【 概要 】 フィットネスクラブの中年層会員 新規獲得向け広告バナーデザインを募集します。 【 依頼内容 】 ・サイズ: 横 × 縦1200×628、1080×1080 ・作成数: 1種類×2サイズ ・納品:制作データ(AIデータまたはPSD)とPNG(指定の2サイズ)をお願いします。 今回1デザインを採用する予定です。たくさんのご応募をお待ちしております! (デザインご提示いただく際、1080×1080のサイズを必ずご提示ください) ・利用用途:バナー広告 【 デザインイメージ 】 ・参考デザイン:検索エンジンに引っかからないようにするため、Googleドキュメントのテキストにて添付いたします。 https://notes.pelvarix.net/sheet/d/7kQmTrazPLuVw2eNc-4Hydxo8Bf52sJ3K9WnLqRT0Yb/view?src=link こちらより参考にしてくださいませ。 【 契約金額(税抜) 】 1デザイン 3,000円 ※契約金額(税込)からシステム利用料を差し引いた金額が、ワーカーさまの受取金額となります その他ご質問等ありましたら、気軽にお問い合わせください。 ご応募をお待ちしております! |
目にとまるカラーで、キャッチも読みやすいバナーでした!
皆さまご提案ありがとうございました!

```html
<!DOCTYPE html>
<html lang="ja">
<head>
<meta charset="utf-8">
<title>50代からの運動習慣・健康習慣 バナー</title>
<link rel="stylesheet" href="https://fonts.googleapis.com/css2?family=Noto+Sans+JP:wght@500;700;900&display=swap">
<style>
  :root {
    --navy: #1f3563;
    --orange: #f28a12;
    --yellow: #ffd23a;
    --white: #ffffff;
    --photo-a: #e9e4dc;
    --photo-b: #c9d3d6;
    --photo-c: #d8b8a6;
  }
  * { margin: 0; padding: 0; box-sizing: border-box; }
  html, body { width: 1200px; height: 1200px; overflow: hidden; background: var(--white); }
  .banner {
    position: relative;
    width: 1200px;
    height: 1200px;
    overflow: hidden;
    font-family: "Noto Sans JP", sans-serif;
    color: var(--navy);
    background: var(--white);
  }
  .hero-photo {
    position: absolute;
    left: 0; top: 0;
    width: 1200px; height: 620px;
    background: linear-gradient(110deg, var(--photo-a) 0%, var(--photo-c) 45%, var(--photo-b) 75%, var(--photo-a) 100%);
  }
  .headline-band {
    position: absolute;
    left: 0; top: 225px;
    width: 1200px; height: 335px;
    background: linear-gradient(90deg, rgba(255,255,255,0.88) 0%, rgba(255,255,255,0.8) 55%, rgba(255,255,255,0.15) 100%);
  }
  .headline-line {
    position: absolute;
    white-space: nowrap;
    font-weight: 700;
    line-height: 1;
  }
  .headline-age { left: 80px; top: 250px; font-size: 80px; }
  .headline-age .num {
    font-size: 140px;
    font-weight: 900;
    font-style: italic;
    margin-right: 6px;
  }
  .headline-habits { left: 70px; top: 440px; font-size: 72px; }
  .underline {
    position: absolute;
    height: 7px;
    background: var(--orange);
  }
  .underline-age { left: 40px; top: 400px; width: 600px; }
  .underline-habits { left: 0; top: 530px; width: 790px; }

  .lead {
    position: absolute;
    white-space: nowrap;
    font-weight: 700;
    line-height: 1;
    display: flex;
    align-items: baseline;
  }
  .lead-years { left: 205px; top: 640px; font-size: 80px; }
  .lead-years .num {
    color: var(--orange);
    font-size: 160px;
    font-weight: 900;
    font-style: italic;
    margin-right: 16px;
  }
  .lead-extend { left: 28px; top: 805px; font-size: 62px; }
  .lead-extend .key {
    color: var(--orange);
    font-size: 92px;
    font-weight: 900;
  }

  .offer-bar {
    position: absolute;
    left: 0; top: 975px;
    width: 1200px; height: 225px;
    background: var(--navy);
  }
  .offer-line {
    position: absolute;
    left: 60px;
    color: var(--white);
    font-weight: 700;
    font-size: 46px;
    line-height: 1;
    white-space: nowrap;
    display: flex;
    align-items: baseline;
  }
  .offer-line-now { top: 1002px; }
  .offer-line-free { top: 1068px; }
  .offer-line .lead-char { font-size: 58px; }
  .offer-line .free {
    color: var(--yellow);
    font-size: 58px;
    margin-left: 4px;
  }
  .offer-line .free .zero {
    font-size: 86px;
    font-style: italic;
    font-weight: 900;
    margin-right: 2px;
  }
  .cta-button {
    position: absolute;
    left: 533px; top: 995px;
    width: 627px; height: 150px;
    border: 3px solid var(--white);
    border-radius: 34px;
    display: flex;
    align-items: center;
    justify-content: center;
    gap: 22px;
    color: var(--white);
    font-weight: 500;
    font-size: 52px;
    white-space: nowrap;
  }
  .cta-button .small { font-size: 44px; }
  .cta-button svg { width: 30px; height: 50px; }
</style>
</head>
<body>
  <main class="banner">
    <div class="hero-photo" role="img" aria-label="明るいスタジオで笑顔でストレッチをする女性たちの写真"></div>
    <div class="headline-band"></div>

    <h1>
      <span class="headline-line headline-age"><span class="num">50</span>代からの</span>
      <span class="headline-line headline-habits">運動習慣・健康習慣</span>
    </h1>
    <span class="underline underline-age"></span>
    <span class="underline underline-habits"></span>

    <p class="lead lead-years"><span class="num">10</span>年後の健康のために</p>
    <p class="lead lead-extend"><span class="key">「健康寿命」</span>を延ばす!</p>

    <section class="offer-bar"></section>
    <p class="offer-line offer-line-now"><span class="lead-char">今</span>なら、入会金</p>
    <p class="offer-line offer-line-free">初月会費が<span class="free"><span class="zero">0</span>円</span></p>
    <div class="cta-button">
      <span>お申込み<span class="small">はこちら</span></span>
      <svg viewBox="0 0 30 50" aria-hidden="true"><polyline points="4,4 26,25 4,46" fill="none" stroke="#ffffff" stroke-width="4"/></svg>
    </div>
  </main>
</body>
</html>
```